LEARN Business Skills so you can Earn a good living

size of the poster is 8”x 10.75" plus 0.25" bleed.
Please leave 1 inch on the bottoum for footer
I want a design a poster that will attract people's attention.
I appreciate a creative ad however the ad should not take away from being able to clearly read the text.
-I also appreciate a simple creative ad that is not too busy.
-you can use graphics, vectors, or pictures of real people.
-however, if you use real people it should be a white male that is wearing a white shirt and look like a professional person.

Target Market(s)

Potential young business people

Industry/Entity Type

education

Requirements
Must have
• easy to read the text
Nice to have
• I would like a "creative" simple ad that is easy to be read
Should not have
• pictures of women

```html
<!DOCTYPE html>
<html lang="en">
<head>
<meta charset="utf-8">
<title>Learn To Earn – Business Enrichment Course</title>
<link href="https://fonts.googleapis.com/css2?family=Poppins:wght@400;700&family=Roboto:wght@500;700&display=swap" rel="stylesheet">
<style>
  :root {
    --paper: #f7fafb;
    --ink: #0b0d0e;
    --accent: #c4202f;
    --texture: #e3e6e8;
    --photo-top: #d9cfb8;
    --photo-bottom: #c9a85a;
  }
  html, body {
    margin: 0;
    padding: 0;
    width: 900px;
    height: 1200px;
    overflow: hidden;
    background: var(--paper);
  }
  .poster {
    position: relative;
    width: 900px;
    height: 1200px;
    overflow: hidden;
    background: var(--paper);
    color: var(--ink);
    font-family: "Poppins", sans-serif;
  }
  .backdrop-texture {
    position: absolute;
    left: 30px;
    top: 110px;
    width: 840px;
    height: 730px;
    background: radial-gradient(ellipse at 50% 50%, var(--texture) 0%, rgba(227,230,232,0.55) 45%, rgba(247,250,251,0) 72%);
  }
  .title {
    position: absolute;
    top: 104px;
    left: 0;
    width: 100%;
    margin: 0;
    text-align: center;
    font-family: "Poppins", sans-serif;
    font-weight: 700;
    font-size: 100px;
    line-height: 1.2;
    letter-spacing: -1px;
  }
  .subtitle {
    position: absolute;
    top: 210px;
    left: 0;
    width: 100%;
    display: flex;
    justify-content: center;
    align-items: center;
    gap: 8px;
    font-size: 29px;
    font-weight: 400;
    letter-spacing: 0.5px;
  }
  .subtitle svg { width: 22px; height: 24px; }
  .hero-photo {
    position: absolute;
    left: 126px;
    top: 300px;
    width: 661px;
    height: 308px;
    background: linear-gradient(180deg, var(--photo-top) 0%, var(--photo-bottom) 100%);
  }
  .quote {
    position: absolute;
    top: 685px;
    left: 0;
    width: 100%;
    text-align: center;
    font-family: "Roboto", sans-serif;
    font-weight: 500;
    font-size: 42px;
    line-height: 49px;
    margin: 0;
  }
  .quote-mark {
    position: absolute;
    width: 66px;
    height: 58px;
  }
  .quote-mark--open { left: 86px; top: 709px; }
  .quote-mark--close { left: 751px; top: 709px; }
  .benefits-heading {
    position: absolute;
    top: 829px;
    left: 0;
    width: 100%;
    margin: 0;
    text-align: center;
    font-family: "Roboto", sans-serif;
    font-weight: 700;
    font-size: 27px;
    color: var(--accent);
  }
  .benefits {
    position: absolute;
    top: 867px;
    left: 0;
    width: 100%;
    text-align: center;
    font-family: "Roboto", sans-serif;
    font-weight: 500;
    font-size: 21.5px;
    margin: 0;
  }
  .divider {
    position: absolute;
    top: 936px;
    left: 383px;
    width: 137px;
    height: 1.5px;
    background: var(--ink);
  }
  .topics {
    position: absolute;
    top: 980px;
    margin: 0;
    padding: 0;
    list-style: none;
    font-size: 15.5px;
    line-height: 19.6px;
  }
  .topics li {
    position: relative;
    padding-left: 12px;
  }
  .topics li::before {
    content: "";
    position: absolute;
    left: 0;
    top: 7px;
    width: 5px;
    height: 5px;
    border-radius: 50%;
    background: var(--accent);
  }
  .topics li.continued::before { display: none; }
  .topics--col1 { left: 64px; }
  .topics--col2 { left: 327px; }
  .topics--col3 { left: 522px; }
  .topics--col4 { left: 727px; }
</style>
</head>
<body>
<main class="poster">
  <div class="backdrop-texture" role="img" aria-label="Faint grey halftone dot texture behind the headline and photo"></div>

  <h1 class="title">Learn To Earn</h1>
  <div class="subtitle">
    <svg viewBox="0 0 20 22" aria-hidden="true"><path d="M3 2 L9 2 L17 11 L9 20 L3 20 L11 11 Z" fill="var(--accent)"/></svg>
    <span>Business Enrichment Course</span>
    <svg viewBox="0 0 20 22" aria-hidden="true"><path d="M17 2 L11 2 L3 11 L11 20 L17 20 L9 11 Z" fill="var(--accent)"/></svg>
  </div>

  <div class="hero-photo" role="img" aria-label="Photo of a stack of gold and silver coins with a miniature businessman sitting on top reading a newspaper"></div>

  <svg class="quote-mark quote-mark--open" viewBox="0 0 66 58" aria-hidden="true">
    <path d="M28 4 C12 10 2 24 4 40 C5 50 10 56 18 56 C25 56 29 51 29 45 C29 38 24 34 18 34 C15 34 13 35 12 36 C13 24 20 14 30 8 Z" fill="var(--accent)"/>
    <path d="M62 4 C46 10 36 24 38 40 C39 50 44 56 52 56 C59 56 63 51 63 45 C63 38 58 34 52 34 C49 34 47 35 46 36 C47 24 54 14 64 8 Z" fill="var(--accent)"/>
  </svg>
  <p class="quote">A proven success of helping<br>people in their livelihoods</p>
  <svg class="quote-mark quote-mark--close" viewBox="0 0 66 58" aria-hidden="true">
    <path d="M4 54 C20 48 30 34 28 18 C27 8 22 2 14 2 C7 2 3 7 3 13 C3 20 8 24 14 24 C17 24 19 23 20 22 C19 34 12 44 2 50 Z" fill="var(--accent)"/>
    <path d="M38 54 C54 48 64 34 62 18 C61 8 56 2 48 2 C41 2 37 7 37 13 C37 20 42 24 48 24 C51 24 53 23 54 22 C53 34 46 44 36 50 Z" fill="var(--accent)"/>
  </svg>

  <h2 class="benefits-heading">Business skills that will help you</h2>
  <p class="benefits">Get A Quality Job &nbsp;|&nbsp; Start/grow Your Business &nbsp;|&nbsp; Increase Your Salary</p>

  <div class="divider"></div>

  <ul class="topics topics--col1">
    <li>Business Admnistration</li>
    <li>Small&nbsp; Business Management</li>
    <li>Finance</li>
    <li>Investments</li>
    <li>Computers</li>
    <li>Accounting</li>
  </ul>
  <ul class="topics topics--col2">
    <li>Sales</li>
    <li>Marketing</li>
    <li>Project Management</li>
    <li class="continued">Interviewing Skills</li>
    <li>Business Law</li>
    <li>Negotiation</li>
  </ul>
  <ul class="topics topics--col3">
    <li>Public Speaking</li>
    <li>Import/export</li>
    <li>Information Technoloy</li>
    <li>Distribution</li>
    <li>Marketing</li>
    <li>Ledgerly</li>
  </ul>
  <ul class="topics topics--col4">
    <li>Real Estate</li>
    <li>Health Care</li>
    <li>Management</li>
    <li>Shopvane</li>
  </ul>
</main>
</body>
</html>
```